2024 Veltmore Financial Team Deck

I have created a power point slide deck and I need the slide deck recreated. Organized, with better color, background pictures, etc. I am thinking the colors for the presentation can be navy blue, and white, and gold, with hints of silver and black. We are financial planning firm that specializes in working with tech companies in silicon valley.

```html
<!DOCTYPE html>
<html lang="en">
<head>
<meta charset="utf-8">
<title>2024 Veltmore Financial Team Deck</title>
<link rel="stylesheet" href="https://fonts.googleapis.com/css2?family=Poppins:wght@400;500;600;700;800&family=Oswald:wght@500;600&family=Montserrat:wght@400;500;600;700&display=swap">
<style>
:root{
  --navy:#0a2f86;
  --deep:#082b7a;
  --blue:#0b45c2;
  --bright:#1557dc;
  --card:#0d4fd4;
  --line:#3aa7ff;
  --white:#ffffff;
  --paper:#ececf1;
  --ink:#0b3aa8;
  --grey:#5b5f6b;
}
*{margin:0;padding:0;box-sizing:border-box}
html,body{width:804px;height:1200px;overflow:hidden}
body{
  position:relative;
  font-family:'Montserrat',sans-serif;
  background:linear-gradient(180deg,#ffffff 0,#ffffff 600px,#dcdcdf 690px,#9c9ca2 900px,#6c6c72 1200px);
}
.slide{position:absolute;overflow:hidden;width:236px;height:133px}
.blue-bg{background:linear-gradient(135deg,#0a3a9e 0%,#0d4cc6 50%,#083490 100%)}
.photo{position:absolute}
.title-slide{width:23.6em;height:13.3em}
.hline,.vline{position:absolute;background:var(--line);box-shadow:0 0 .3em var(--line)}
.hline{left:0;right:0;height:.18em}
.vline{top:0;bottom:0;width:.18em}
.title-text{position:absolute;inset:0;display:flex;flex-direction:column;align-items:center;justify-content:center;color:var(--white);font-family:'Poppins',sans-serif;font-weight:700;font-size:2em;line-height:1.15;text-align:center}
.hero{left:180px;top:40px;font-size:24.6px}
.hero .title-text{font-size:2.2em}
.goals-slide{width:23.6em;height:13.3em;background:var(--paper)}
.goals-title{position:absolute;top:.7em;left:0;right:0;text-align:center;font-family:'Oswald',sans-serif;font-weight:600;color:var(--deep);font-size:1.45em;line-height:1.02}
.goals-band{position:absolute;top:7.6em;bottom:0;width:6.2em}
.goal-card{position:absolute;top:6.2em;width:4em;height:5.7em;background:var(--white);border:.15em solid var(--navy);display:flex;flex-direction:column;align-items:center;justify-content:center;text-align:center;font-family:'Oswald',sans-serif;font-weight:600;color:var(--deep);line-height:.95}
.goal-card .big{font-size:2em}
.goal-card .small{font-size:1.05em}
.goals-hero{left:40px;top:300px;font-size:14px;box-shadow:0 6px 18px rgba(0,0,0,.25)}
.band-title{position:absolute;left:0;right:0;top:0;height:31px;background:var(--white);color:var(--bright);font-weight:700;font-size:16px;text-align:center;line-height:31px;white-space:nowrap}
.band-body{position:absolute;left:0;right:0;top:31px;height:92px}
.org-box{position:absolute;background:var(--white);border-radius:4px;color:#222;text-align:center;font-size:7.5px;line-height:1.1;display:flex;flex-direction:column;justify-content:center;border:1px solid var(--white)}
.org-box .role{padding:2px}
.org-box .who{background:var(--card);color:var(--white);font-weight:700;font-size:4.6px;padding:2px 1px;margin:0 2px 2px;border-radius:2px}
.mission-panel{position:absolute;left:116px;top:0;width:120px;height:133px;background:var(--white)}
.mission-top{position:absolute;left:0;right:0;top:0;height:44px;background:var(--blue);color:var(--white);text-align:right;padding:4px 6px 0}
.mission-top h3{font-family:'Poppins',sans-serif;font-weight:800;font-size:13px;line-height:.95}
.tiny{font-size:3.3px;line-height:1.25}
.mission-mid{position:absolute;left:0;right:0;top:46px;height:46px;padding:0 6px;text-align:right;color:var(--grey);overflow:hidden}
.mission-mid h4{color:var(--ink);font-weight:700;font-size:7.6px;line-height:1.2}
.mission-mid p{font-size:4.9px;line-height:1.18}
.mission-how{position:absolute;left:0;right:0;top:93px;bottom:0;background:var(--blue);color:var(--white);text-align:right;padding:2px 6px}
.mission-how h4{font-size:7px;font-weight:700}
.vision-head{position:absolute;left:143px;top:14px;color:var(--ink);font-family:'Poppins',sans-serif;font-weight:800;font-size:21px;line-height:.92}
.vision-head span{display:block;font-family:'Montserrat',sans-serif;font-size:6px;color:#222;font-weight:600;margin-top:3px}
.vision-list{position:absolute;left:5px;top:74px;width:133px;list-style:none;color:#333;font-size:3.3px;line-height:1.3}
.vision-list li{margin-bottom:2px;padding-left:4px;position:relative}
.vision-list li::before{content:"";position:absolute;left:0;top:1.3px;width:1.6px;height:1.6px;background:var(--navy);border-radius:50%}
.tab-title{position:absolute;top:0;background:var(--white);color:var(--bright);font-weight:700;text-align:center;white-space:nowrap}
.card{position:absolute;background:var(--card);border:1px solid #3a74e8;border-radius:4px;color:var(--white);padding:3px 9px}
.card h4{font-weight:700;font-size:11px;line-height:1}
.card ul{list-style:none;font-size:5.6px;line-height:1.2;margin-top:1px}
.card li::before{content:"• "}
.tag{position:absolute;left:0;right:0;top:1146px;text-align:center;color:var(--white);font-weight:700;font-size:31px;line-height:1;letter-spacing:.5px;white-space:nowrap}
</style>
</head>
<body>

<section class="slide blue-bg title-slide hero">
  <div class="hline" style="top:2.1em"></div>
  <div class="hline" style="top:11em"></div>
  <div class="vline" style="left:.5em"></div>
  <div class="vline" style="left:22.5em"></div>
  <h1 class="title-text">Veltmore Financial<br>2024</h1>
</section>

<section class="slide goals-slide goals-hero">
  <h2 class="goals-title">2024 FIRM<br>AWARDS/ CALENDAR<br>YEAR GOALS</h2>
  <div class="goals-band" style="left:2.3em;background:var(--bright)"></div>
  <div class="goals-band" style="left:8.5em;background:var(--navy)"></div>
  <div class="goals-band" style="left:14.7em;background:#0a237a"></div>
  <div class="goal-card" style="left:3.4em"><span class="big">$1M</span><span class="small">PREMIUM</span></div>
  <div class="goal-card" style="left:9.6em"><span class="big">$18M</span><span class="small">IN NEW<br>AUM</span></div>
  <div class="goal-card" style="left:15.8em"><span class="big">60</span><span class="big" style="font-size:1.5em">NEW</span><span class="small">CLIENT</span></div>
</section>

<section class="slide blue-bg title-slide" style="left:31px;top:697px;font-size:10px">
  <div class="hline" style="top:2.1em"></div>
  <div class="hline" style="top:11em"></div>
  <div class="vline" style="left:.5em"></div>
  <div class="vline" style="left:22.5em"></div>
  <h2 class="title-text">Veltmore Financial<br>2024</h2>
</section>

<section class="slide" style="left:290px;top:697px;background:var(--white)">
  <div class="photo" role="img" aria-label="Photo of a hand holding a pen over printed financial charts" style="left:0;top:0;width:116px;height:133px;background:linear-gradient(120deg,#3a2a22,#8a6a55 45%,#d8dce4 70%,#8fb3e6)"></div>
  <div class="mission-panel">
    <div class="mission-top">
      <h3>Mission<br>Statement</h3>
      <p class="tiny">To provide our client with the systems and processes needed to guide their Hero's journey and leave an Impact</p>
    </div>
    <div class="mission-mid">
      <h4>THE HERO'S JOURNEY:</h4>
      <p>We believe everyone has a purpose, God's purpose in their life, and it is our mission to help our clients relentlessly pursue their purpose. A life with purpose is a life living out your Hero's Journey!</p>
    </div>
    <div class="mission-how">
      <h4>HOW:</h4>
      <p class="tiny">Our planning services give clients more time and clarity.<br>We help clients think bigger and stay accountable.<br>We reduce taxes, diversify and manage risk.<br>We maximize potential and leave a larger impact.</p>
    </div>
  </div>
</section>

<section class="slide" style="left:547px;top:697px;background:var(--white)">
  <div class="photo" role="img" aria-label="Photo of a professional reviewing data on a tablet with chart overlays" style="left:0;top:0;width:142px;height:70px;background:linear-gradient(135deg,#0d2a6e,#2f6fc4 50%,#9cc6ef)"></div>
  <h2 class="vision-head">Firm<br>Vision<span>(December 2026)</span></h2>
  <ul class="vision-list">
    <li>We are an elite wealth management firm focused on tech clients.</li>
    <li>We serve over 300 households across the Bay Area.</li>
    <li>Each advisor serves a dozen new clients every year.</li>
    <li>The team travels together once a year on a retreat.</li>
    <li>We are healthy, fit and happy in our work.</li>
  </ul>
  <div class="photo" role="img" aria-label="Photo of a desk with laptop, coffee cup and plant" style="left:142px;top:70px;width:94px;height:63px;background:linear-gradient(135deg,#f4f4f2,#cfd3d6 50%,#7e8a86)"></div>
</section>

<section class="slide" style="left:31px;top:845px;background:var(--white)">
  <h2 class="band-title">CURRENT ORG CHART</h2>
  <div class="band-body blue-bg">
    <svg width="236" height="92" style="position:absolute;left:0;top:0">
      <path d="M118 22 V30 M81 30 H161 M81 30 V42 M161 30 V42" stroke="#fff" stroke-width="1.2" fill="none"/>
    </svg>
    <div class="org-box" style="left:91px;top:4px;width:58px;height:18px">DANIEL</div>
    <div class="org-box" style="left:53px;top:38px;width:58px;height:18px">MARA</div>
    <div class="org-box" style="left:132px;top:38px;width:58px;height:18px">OKAFOR</div>
  </div>
</section>

<section class="slide" style="left:290px;top:845px;background:var(--white)">
  <h2 class="band-title">FUTURE ORG CHART</h2>
  <div class="band-body blue-bg">
    <svg width="236" height="92" style="position:absolute;left:0;top:0">
      <path d="M118 28 V38 M30 38 H204 M30 38 V50 M90 38 V50 M147 38 V50 M204 38 V50" stroke="#fff" stroke-width="1.2" fill="none"/>
    </svg>
    <div class="org-box" style="left:90px;top:10px;width:57px;height:20px"><span class="role" style="padding:1px">PRESIDENT</span><span class="who">DANIEL HARLOW</span></div>
    <div class="org-box" style="left:6px;top:50px;width:52px;height:28px;font-size:5px"><span class="role">PRIVATE WEALTH ADVISOR</span><span class="who">(GRU)</span></div>
    <div class="org-box" style="left:64px;top:50px;width:52px;height:32px;font-size:5px"><span class="role">DIRECTOR OF INSURANCE &amp; PLANNING</span><span class="who">MARIANNE</span></div>
    <div class="org-box" style="left:121px;top:50px;width:52px;height:32px;font-size:5px"><span class="role">DIRECTOR OF INVESTMENTS &amp; PLANNING</span><span class="who">OKAFOR</span></div>
    <div class="org-box" style="left:178px;top:50px;width:52px;height:28px;font-size:5px"><span class="role">COO</span><span class="who">THEO BRENNAN</span></div>
  </div>
</section>

<section class="slide blue-bg" style="left:547px;top:845px">
  <div class="hline" style="top:22px;height:2px"></div>
  <div class="hline" style="top:108px;height:2px"></div>
  <div class="vline" style="left:206px;width:2px"></div>
  <h2 style="position:absolute;left:16px;top:44px;color:var(--white);font-family:'Poppins',sans-serif;font-weight:700;font-size:18px;line-height:1.1">Responsibilities /<br>Vital Functions</h2>
</section>

<section class="slide blue-bg" style="left:31px;top:993px">
  <h2 class="tab-title" style="left:35px;width:166px;height:27px;line-height:27px;font-size:8.6px">LEADERSHIP RESPONSIBILITIES</h2>
  <div class="card" style="left:20px;top:28px;width:95px;height:47px"><h4>DANIEL</h4><ul><li>Serving A+ A Clients</li></ul></div>
  <div class="card" style="left:121px;top:28px;width:96px;height:47px"><h4>OKAFOR</h4><ul><li>Servicing B &amp; C Clients</li><li>New Investments account onboarding</li><li>Case Prep</li></ul></div>
  <div class="card" style="left:20px;top:80px;width:95px;height:48px"><h4>MARA</h4><ul><li>Daniel's Calendar Management</li><li>Insurance Operations</li><li>Annual Reviews</li></ul></div>
  <div class="card" style="left:121px;top:80px;width:96px;height:48px"><h4>THEO</h4><ul><li>Posting and Planning</li><li>Goal Tracking</li></ul></div>
</section>

<section class="slide blue-bg" style="left:290px;top:993px">
  <h2 class="tab-title" style="left:35px;width:166px;height:24px;line-height:26px;font-size:10.4px">TEAM WEEKLY CALENDAR</h2>
  <div class="card" style="left:19px;top:25px;width:96px;height:33px"><h4>MONDAY</h4><ul style="font-size:4.3px"><li>Team Meeting</li><li>Daniel No meetings Monday 8-12pm</li></ul></div>
  <div class="card" style="left:120px;top:25px;width:96px;height:33px"><h4>TUESDAY</h4><ul style="font-size:4.6px"><li>Underwriting Emails</li></ul></div>
  <div class="card" style="left:19px;top:62px;width:96px;height:33px"><h4>WEDNESDAY</h4><ul style="font-size:4.6px"><li>OCI Emails</li></ul></div>
  <div class="card" style="left:120px;top:62px;width:96px;height:33px"><h4>THURSDAY</h4><ul style="font-size:4.3px"><li>Team professional development</li></ul></div>
  <div class="card" style="left:72px;top:99px;width:96px;height:31px"><h4>FRIDAY:</h4></div>
</section>

<section class="slide goals-slide" style="left:547px;top:993px;font-size:10px">
  <h2 class="goals-title">2024 FIRM<br>AWARDS/ CALENDAR<br>YEAR GOALS</h2>
  <div class="goals-band" style="left:2.3em;background:var(--bright)"></div>
  <div class="goals-band" style="left:8.5em;background:var(--navy)"></div>
  <div class="goals-band" style="left:14.7em;background:#0a237a"></div>
  <div class="goal-card" style="left:3.4em"><span class="big">$1M</span><span class="small">PREMIUM</span></div>
  <div class="goal-card" style="left:9.6em"><span class="big">$18M</span><span class="small">IN NEW<br>AUM</span></div>
  <div class="goal-card" style="left:15.8em"><span class="big">60</span><span class="big" style="font-size:1.5em">NEW</span><span class="small">CLIENT</span></div>
</section>

<p class="tag">WILL MAKE OTHER TEMPLATES</p>

</body>
</html>
```